Can you create a Business Card based on the Logo you designed.

See example and would like to see other examples.

Trying to keep it very clean with a focus on the logo and name.

```html
<!DOCTYPE html>
<html lang="en">
<head>
<meta charset="utf-8">
<title>Verdano Business Card</title>
<link href="https://fonts.googleapis.com/css2?family=Montserrat:wght@400;500;700&display=swap" rel="stylesheet">
<style>
  :root {
    --stage: #1f1f1f;
    --card-green: #127a45;
    --card-green-light: #1a8a50;
    --emboss-green: #4fa77a;
    --accent-orange: #e8923a;
    --text-white: #ffffff;
  }
  * { box-sizing: border-box; margin: 0; padding: 0; }
  html, body {
    width: 1200px; height: 900px; overflow: hidden;
    background: var(--stage);
    font-family: "Montserrat", sans-serif;
  }
  .stage {
    position: relative; width: 1200px; height: 900px;
  }
  .card {
    position: absolute; left: 250px; width: 700px; height: 400px;
    background: var(--card-green);
    border-radius: 26px;
    overflow: hidden;
    color: var(--text-white);
  }
  .card--front { top: 40px; }
  .card--back { top: 460px; }

  .front-wordmark {
    position: absolute; inset: 0;
    display: flex; align-items: center; justify-content: center;
    font-weight: 700; font-size: 78px; letter-spacing: 1px;
    color: var(--emboss-green);
  }

  .back-decor {
    position: absolute; right: -70px; bottom: -90px;
    width: 300px; height: 300px; border-radius: 50%;
    background: var(--card-green-light);
  }
  .holder {
    position: absolute; top: 42px; right: 46px; text-align: right;
  }
  .holder__name { font-weight: 700; font-size: 27px; letter-spacing: 0.5px; }
  .holder__title { font-weight: 400; font-size: 15px; margin-top: 4px; }

  .brand {
    position: absolute; left: 46px; top: 112px;
    display: flex; align-items: center; gap: 12px;
  }
  .brand__dot {
    width: 18px; height: 18px; border-radius: 50%;
    background: var(--accent-orange);
  }
  .brand__name { font-weight: 700; font-size: 50px; color: var(--text-white); }

  .address {
    position: absolute; left: 46px; top: 226px;
    font-size: 15px; line-height: 1.4; font-weight: 500;
  }
  .contacts {
    position: absolute; left: 46px; top: 290px; list-style: none;
    font-size: 15px; font-weight: 500;
  }
  .contacts li { display: flex; align-items: center; gap: 12px; height: 26px; }
  .contacts svg { width: 15px; height: 15px; fill: var(--text-white); }
</style>
</head>
<body>
<main class="stage">
  <section class="card card--front" aria-label="Card front">
    <div class="front-wordmark">Verdano</div>
  </section>

  <section class="card card--back" aria-label="Card back">
    <div class="back-decor"></div>
    <div class="holder">
      <div class="holder__name">Marcus Ellery</div>
      <div class="holder__title">Chief Executive Officer</div>
    </div>
    <div class="brand">
      <span class="brand__dot"></span>
      <span class="brand__name">Verdano</span>
    </div>
    <p class="address">418 Meadow Lane, #112<br>Fairbrook, OH 43190</p>
    <ul class="contacts">
      <li>
        <svg viewBox="0 0 24 24" aria-hidden="true"><path d="M6.6 10.8a15.1 15.1 0 0 0 6.6 6.6l2.2-2.2a1 1 0 0 1 1-.25 11.4 11.4 0 0 0 3.6.57 1 1 0 0 1 1 1V20a1 1 0 0 1-1 1A17 17 0 0 1 3 4a1 1 0 0 1 1-1h3.5a1 1 0 0 1 1 1c0 1.25.2 2.45.57 3.57a1 1 0 0 1-.25 1z"/></svg>
        +1 (555) 210-4478
      </li>
      <li>
        <svg viewBox="0 0 24 24" aria-hidden="true"><path d="M2 5h20v14H2zm2 2v.4l8 5.2 8-5.2V7zm0 2.8V17h16V9.8l-8 5.2z"/></svg>
        ceo@verdano.com
      </li>
      <li>
        <svg viewBox="0 0 24 24" aria-hidden="true"><path d="M12 2a10 10 0 1 0 0 20 10 10 0 0 0 0-20zm6.9 6h-2.9a15.7 15.7 0 0 0-1.4-3.6A8 8 0 0 1 18.9 8zM12 4a14 14 0 0 1 1.9 4h-3.8A14 14 0 0 1 12 4zM4.3 14a8 8 0 0 1 0-4h3.4a16.5 16.5 0 0 0 0 4zm.8 2h2.9a15.7 15.7 0 0 0 1.4 3.6A8 8 0 0 1 5.1 16zM8 8H5.1a8 8 0 0 1 4.3-3.6A15.7 15.7 0 0 0 8 8zm4 12a14 14 0 0 1-1.9-4h3.8A14 14 0 0 1 12 20zm2.3-6H9.7a14.7 14.7 0 0 1 0-4h4.6a14.7 14.7 0 0 1 0 4zm.3 5.6a15.7 15.7 0 0 0 1.4-3.6h2.9a8 8 0 0 1-4.3 3.6zm1.7-5.6a16.5 16.5 0 0 0 0-4h3.4a8 8 0 0 1 0 4z"/></svg>
        www.verdano.com
      </li>
    </ul>
  </section>
</main>
</body>
</html>
```